Home page web design for "Tales from Thee"

We need a home page web design for a start up company that will write memoirs for seniors.
The completed project will need to include PSD files...NO HTML or CSS necessary.
Attached is a brief outline concept that may give you some ideas...but you are the creative professionals, so please feel free to add your ideas. We will also attach some files that show you our logo, brochures, and photos that could be used to give you ideas of our focus.
There will need to be access to the other pages on the home page to include: 'About Us'; 'How We Can Help'; 'Community Sessions'; 'Senior Consulting ' and 'Contact Us'.
Updates

Target Market(s)

Seniors and Baby Boomers

Industry/Entity Type

It Company

Number of Pages Required

1 page

Colors
f9ba93
fbca95
faa54b
faf289
f37123

Requirements
Must have
• Script easy on senior eyes.
• Initial contact number would be 844-4LANTERN
Nice to have
• While the color pallet is non-specific we prefer the warm colors.
• salmon, peach.......
• NOT so much the orange of Halloween:)
• However, please utilize your creativity and put in colors you feel will draw best with your design.

```html
<!DOCTYPE html>
<html lang="en">
<head>
<meta charset="utf-8">
<title>Tales from Thee – Home</title>
<link href="https://fonts.googleapis.com/css2?family=Gelasio:ital,wght@0,400;0,700;1,400;1,700&family=Varela+Round&family=Lato:wght@400;700&display=swap" rel="stylesheet">
<style>
:root{
  --salmon:#f9957b;
  --salmon-light:#f9ba93;
  --peach:#fbca95;
  --orange:#f37123;
  --orange-soft:#faa54b;
  --pink:#f9c9c4;
  --ink:#2a2a2a;
  --ink-soft:#4a3a32;
  --white:#ffffff;
  --page:#fbfbf8;
  --gold:#b8913a;
}
*{margin:0;padding:0;box-sizing:border-box}
html,body{width:1055px;height:1200px;overflow:hidden}
body{background:var(--page);font-family:"Gelasio",Georgia,serif;color:var(--ink);position:relative}
.canvas{position:relative;width:1055px;height:1200px;overflow:hidden;
  background:linear-gradient(180deg,#eaf4f8 0,var(--page) 140px,var(--page) 100%)}
.shapes{position:absolute;left:0;top:0}

/* header */
.brand-oval{position:absolute;left:46px;top:16px;width:288px;height:136px;border-radius:50%;
  background:var(--white);border:3px solid #f3ead8;box-shadow:0 2px 8px rgba(0,0,0,.08);
  display:flex;align-items:center;justify-content:center}
.brand-name{font-family:"Gelasio",Georgia,serif;font-size:25px;font-weight:400;color:var(--gold)}
.main-nav{position:absolute;left:324px;top:72px;width:684px;height:42px;background:var(--salmon);
  display:flex;align-items:center;justify-content:space-around;padding:0 6px}
.main-nav a{font-family:"Varela Round",sans-serif;font-size:12.5px;text-transform:uppercase;color:var(--ink-soft);text-decoration:none;letter-spacing:.2px}

/* hero */
.photo{position:absolute}
.photo-left{left:60px;top:192px;width:310px;height:330px;border-radius:16px 0 0 0;
  background:linear-gradient(135deg,#e9eef2 0%,#cfd8e0 40%,#8fa1b3 75%,#c7b4a6 100%)}
.photo-right{left:680px;top:192px;width:316px;height:340px;border-radius:0 16px 0 0;
  background:linear-gradient(135deg,#5a2d1c 0%,#8a4a2a 35%,#b6845e 65%,#d9c2ae 100%)}
.hero-text{position:absolute;left:356px;top:206px;width:334px;text-align:center;color:var(--white)}
.hero-title{font-size:33px;font-style:italic;font-weight:400;line-height:1.2}
.hero-lead{margin-top:20px;font-size:18px;font-style:italic;font-weight:700;line-height:1.4}

/* intro */
.headline{position:absolute;left:0;top:660px;width:1055px;text-align:center;font-size:43px;font-style:italic;font-weight:400;color:var(--orange)}
.intro{position:absolute;left:44px;top:752px;width:966px;text-align:center;font-size:15.4px;line-height:1.55;color:var(--ink)}
.intro p{margin-bottom:18px}
.intro .quote{color:var(--orange-soft);font-style:italic;font-weight:700}
.scene-couple{position:absolute;left:590px;top:790px;width:450px;height:250px;
  background:radial-gradient(ellipse at 50% 55%,rgba(214,205,196,.55) 0%,rgba(232,226,220,.3) 45%,rgba(251,251,248,0) 75%)}

/* footer */
.bench{position:absolute;left:240px;top:1030px;width:180px;height:88px;border-radius:4px;
  background:linear-gradient(180deg,#8c8c86 0%,#6d6b64 100%)}
.footer-oval{position:absolute;left:852px;top:1020px;width:158px;height:74px;border-radius:50%;
  background:var(--white);border:2px solid #f3ead8;display:flex;align-items:center;justify-content:center}
.footer-oval .brand-name{font-size:15px}
.contact{position:absolute;left:46px;top:1104px;color:var(--white);font-family:"Lato",sans-serif}
.contact-name{font-family:"Gelasio",Georgia,serif;font-weight:700;font-size:17px;margin-bottom:6px}
.contact-row{display:flex;align-items:center;gap:10px;font-size:14.5px;font-weight:700;height:22px}
.contact-row.email{font-weight:400;font-size:13px}
.contact-row svg{width:13px;height:13px;flex:none}
.footer-nav{position:absolute;right:46px;top:1106px;display:flex;gap:0;font-family:"Lato",sans-serif;font-size:12px}
.footer-nav a{color:var(--ink-soft);text-decoration:none;padding:0 9px;border-left:1px solid rgba(255,255,255,.6)}
.footer-nav a:first-child{border-left:none}
.copyright{position:absolute;right:46px;top:1138px;font-family:"Lato",sans-serif;font-size:12px;color:var(--ink-soft)}
.social{position:absolute;right:44px;top:1166px;display:flex;gap:10px}
.social span{width:21px;height:21px;border-radius:50%;background:var(--white);display:block}
</style>
</head>
<body>
<div class="canvas">

  <svg class="shapes" width="1055" height="1200" viewBox="0 0 1055 1200" aria-hidden="true">
    <defs>
      <linearGradient id="panelFill" x1="0" y1="0" x2="0" y2="1">
        <stop offset="0" stop-color="#f37123"/>
        <stop offset="1" stop-color="#f68a3a"/>
      </linearGradient>
    </defs>
    <!-- hero card -->
    <rect x="44" y="180" width="966" height="414" rx="20" fill="#ffffff" stroke="#ececec" stroke-width="2"/>
    <!-- footer band -->
    <path d="M0 996 C 180 1050, 360 1040, 540 1040 C 720 1040, 860 992, 1055 984 L1055 1200 L0 1200 Z" fill="#f9957b"/>
  </svg>

  <header>
    <div class="brand-oval"><span class="brand-name">Tales from Thee</span></div>
    <nav class="main-nav">
      <a href="#">About</a>
      <a href="#">How We Can Help</a>
      <a href="#">Community Services</a>
      <a href="#">Senior Consulting Services</a>
      <a href="#">Contact</a>
    </nav>
  </header>

  <section class="hero">
    <div class="photo photo-left" role="img" aria-label="Photo of a grandfather reading a book with a baby on his lap"></div>
    <div class="photo photo-right" role="img" aria-label="Photo of an elderly woman writing at a desk in a warm study"></div>
    <svg class="shapes" width="1055" height="1200" viewBox="0 0 1055 1200" aria-hidden="true">
      <path d="M60 462 C 180 520, 300 522, 380 498 L380 570 L78 570 Q60 570 60 552 Z" fill="#f37b2c"/>
      <path d="M60 490 C 180 540, 300 540, 380 520" fill="none" stroke="#fbca95" stroke-width="3"/>
      <path d="M680 548 C 800 530, 900 512, 996 508 L996 552 Q996 570 978 570 L680 570 Z" fill="#f9c9c4"/>
      <path d="M680 540 C 800 520, 900 502, 996 498" fill="none" stroke="#faa54b" stroke-width="5"/>
      <path d="M356 192 L690 192 Q676 380 690 564 L528 624 L366 564 Q340 380 356 192 Z" fill="url(#panelFill)"/>
    </svg>
    <div class="hero-text">
      <h1 class="hero-title">“When a genealogy doesn’t say enough!”</h1>
      <p class="hero-lead">If you were alive in 100 years, what would you share with your descendants?</p>
      <p class="hero-lead">Now you have a vehicle to help you immortalize your thoughts for the future...specifically for those who will want to know!</p>
    </div>
  </section>

  <main>
    <div class="scene-couple" role="img" aria-label="Faded photo of a bride and groom walking hand in hand on a beach"></div>
    <h2 class="headline">Ordinary Lives............Extraordinary Legacies</h2>
    <div class="intro">
      <p>We are not all presidents of countries or CEO’s of fortune 500 companies! But <span class="quote">“every life legacy is a gift to be treasured by the next generation.”</span></p>
      <p>Does your family host generations of soldiers, doctors, farmers, scientists, mechanics, entrepreneurs, writers, politicians, contractors, pastors, artisans, athletes, musicians, etc..? Generational patterns can often emerge when writing your story that will interest the next generation.</p>
      <p>A genealogy, while very relevant, doesn’t offer the personal story of the names we find. A biography can place a deeper relevance on the face for future descendants. Every life is a legacy to pass forward and we at Tales from Thee believe everyone should chronicle their life journey in writing. This commitment allows you to be remembered for who you truly are as a person.</p>
      <p>Think about it....Do you know the triumphs and tribulations of your ancestors? Do you wish you did? Well, so will those falling into your personal family tree</p>
    </div>
  </main>

  <footer>
    <div class="bench" role="img" aria-label="Illustration of a wooden park bench with an open book"></div>
    <div class="footer-oval"><span class="brand-name">Tales from Thee</span></div>
    <div class="contact">
      <div class="contact-name">Helen Marlowe M.A</div>
      <div class="contact-row">
        <svg viewBox="0 0 16 16"><path d="M3 1 L6 1 L7 5 L5 6 C6 8.5 7.5 10 10 11 L11 9 L15 10 L15 13 C15 14 14 15 13 15 C6.5 15 1 9.5 1 3 C1 2 2 1 3 1 Z" fill="#fff"/></svg>
        <span>717 - 555 - 0142</span>
      </div>
      <div class="contact-row">
        <svg viewBox="0 0 16 16"><circle cx="8" cy="8" r="6.5" fill="none" stroke="#fff" stroke-width="1.6"/><path d="M8 4 L8 8 L11 10" fill="none" stroke="#fff" stroke-width="1.6"/></svg>
        <span>844-4LANTERN</span>
      </div>
      <div class="contact-row email">
        <svg viewBox="0 0 16 16"><rect x="1" y="3" width="14" height="10" fill="none" stroke="#fff" stroke-width="1.4"/><path d="M1 3 L8 9 L15 3" fill="none" stroke="#fff" stroke-width="1.4"/></svg>
        <span>info@talesfromthee.com</span>
      </div>
    </div>
    <nav class="footer-nav">
      <a href="#">Home</a>
      <a href="#">About</a>
      <a href="#">How We Can Help</a>
      <a href="#">Community Services</a>
      <a href="#">Senior Consulting Services</a>
      <a href="#">Contact</a>
    </nav>
    <p class="copyright">© 2014 Willow Quill Studio. | All Rights Reserved</p>
    <div class="social" aria-label="Social links"><span></span><span></span><span></span><span></span></div>
  </footer>

</div>
</body>
</html>
```